10 Page Marketing Report Template - Cindermoor Care Allies

https://www.vidquill.example/share/7f1e9c04b2d84a61a5c3e9d02b6f4a17

We are creating a professional, modern, and slightly edgy PDF-style report document (about 10 pages) to showcase the results of a client’s first 30 days with Cindermoor Care Allies.

The report will be designed as a customizable Plakkit template so the Client Success team can easily update logos, screenshots, and text for each client.

This document will serve as both a visual presentation piece and a report deliverable, blending clean design, modern layout, and data-driven storytelling.

I am attaching the content for the report doc and the design brief along with the logo.
Here is our website for design style, look, and feel: https://cindermoorcare.example/

Here is a quick overview video I made:

```html
<!DOCTYPE html>
<html lang="en">
<head>
<meta charset="utf-8">
<title>30 Days to Value Report – Cindermoor Care Allies</title>
<link href="https://fonts.googleapis.com/css2?family=Poppins:wght@800;900&family=Source+Sans+3:wght@400;600&display=swap" rel="stylesheet">
<style>
  :root {
    --navy: #050818;
    --ink: #0b0f24;
    --blue: #4aa5ec;
    --blue-card: #51a8ee;
    --blue-soft: #b9dbf6;
    --paper: #ffffff;
    --backdrop: #cbcbcb;
    --text: #1a1c28;
  }
  * { box-sizing: border-box; margin: 0; padding: 0; }
  html, body { width: 947px; height: 1200px; overflow: hidden; }
  body {
    background: var(--backdrop);
    font-family: "Source Sans 3", sans-serif;
    color: var(--text);
    position: relative;
  }
  .page {
    position: absolute;
    width: 437px;
    height: 565px;
    overflow: hidden;
    background: var(--paper);
  }
  .page--cover { left: 30px; top: 32px; background: var(--navy); }
  .page--welcome { left: 481px; top: 32px; height: 570px; }
  .page--highlights { left: 30px; top: 612px; }
  .page--audits { left: 481px; top: 612px; }

  /* brand mark stand-in */
  .brand { display: flex; align-items: center; gap: 4px; }
  .brand__square { width: 8px; height: 8px; background: var(--blue); }
  .brand__name {
    font-size: 6.5px; font-weight: 600; color: var(--ink);
    line-height: 1.05; width: 52px; text-transform: uppercase; letter-spacing: .2px;
  }

  /* running header */
  .page-header {
    position: absolute; left: 16px; right: 14px; top: 12px; height: 28px;
    border-bottom: 1px solid var(--blue);
  }
  .page-header .brand { position: absolute; left: 0; top: 2px; }
  .page-header__tag {
    position: absolute; right: 0; bottom: 2px; font-size: 6.5px; color: var(--ink);
  }

  .section-title {
    position: absolute; font-family: "Poppins", sans-serif; font-weight: 900;
    color: var(--blue); text-transform: uppercase; line-height: 1.08; letter-spacing: -.6px;
  }

  /* cover */
  .cover__waves {
    position: absolute; inset: 0;
    background:
      radial-gradient(ellipse 60% 45% at 75% 85%, rgba(74,165,236,.35), transparent 70%),
      radial-gradient(ellipse 45% 35% at 35% 40%, rgba(74,165,236,.15), transparent 70%);
  }
  .cover__client-logo {
    position: absolute; left: 40px; top: 22px; width: 184px; height: 72px;
    background: var(--paper); display: flex; align-items: center; justify-content: center;
    font-size: 7px; color: var(--ink);
  }
  .cover__title {
    position: absolute; left: 40px; top: 166px;
    font-family: "Poppins", sans-serif; font-weight: 900; color: var(--blue);
    font-size: 66px; line-height: .88; letter-spacing: -3px; text-transform: uppercase;
  }
  .cover__report {
    position: absolute; left: 362px; top: 284px; transform-origin: left top; transform: rotate(-90deg);
    font-family: "Poppins", sans-serif; font-weight: 900; color: var(--paper);
    font-size: 28px; letter-spacing: .5px; line-height: 1;
  }
  .cover__rule { position: absolute; left: 40px; top: 287px; width: 354px; height: 1px; background: var(--blue); }
  .cover__subtitle {
    position: absolute; left: 54px; top: 288px;
    font-family: "Poppins", sans-serif; font-weight: 800; color: var(--paper); font-size: 19px; letter-spacing: -.4px;
  }
  .cover__meta {
    position: absolute; left: 42px; top: 335px; width: 162px; height: 32px; background: var(--paper);
    padding: 5px 3px; font-size: 6px; line-height: 1.9; color: var(--ink);
  }
  .cover__brand-box {
    position: absolute; left: 42px; top: 374px; width: 66px; height: 43px; background: var(--paper);
    display: flex; align-items: center; justify-content: center;
  }
  .cover__brand-box .brand__name { width: 44px; font-size: 5.5px; }
  .cover__prepared { position: absolute; left: 44px; top: 421px; font-size: 6px; line-height: 1.4; color: var(--paper); }
  .cover__prepared span { color: var(--blue); display: block; }

  /* welcome */
  .welcome__body { position: absolute; left: 45px; top: 124px; width: 225px; font-size: 7.6px; line-height: 1.5; }
  .welcome__body p + p { margin-top: 10px; }
  .welcome__photo { position: absolute; left: 0; top: 0; width: 437px; height: 570px; }

  /* highlights */
  .highlights__glow {
    position: absolute; left: 0; right: 0; bottom: 0; height: 420px;
    background: linear-gradient(to bottom, rgba(74,165,236,0) 0%, rgba(74,165,236,.35) 55%, rgba(74,165,236,.9) 100%);
  }
  .win-card {
    position: absolute; width: 106px; height: 152px; background: var(--blue-card);
    box-shadow: 3px 4px 8px rgba(0,0,0,.35); padding: 14px 13px;
  }
  .win-card svg { display: block; width: 34px; height: 34px; margin: 6px auto 0 20px; }
  .win-card__text { position: absolute; left: 14px; right: 10px; top: 73px; font-size: 7.6px; line-height: 1.5; color: var(--paper); }
  .win-card--low .win-card__text { top: 75px; }

  /* audits */
  .audits__intro { position: absolute; left: 56px; top: 127px; width: 340px; font-size: 7.6px; line-height: 1.5; }
  .audits__heading {
    position: absolute; left: 0; right: 0; top: 197px; text-align: center;
    font-family: "Poppins", sans-serif; font-weight: 800; font-size: 11.5px; color: var(--ink); letter-spacing: -.3px;
  }
  .funnel-step {
    position: absolute; height: 43px; background: var(--ink); color: var(--paper);
    display: flex; flex-direction: column; align-items: center; justify-content: center;
    text-align: center; font-size: 7.4px; line-height: 1.45;
  }
  .funnel-step__label { color: var(--blue); text-transform: uppercase; }
</style>
</head>
<body>

<!-- Page 1: cover -->
<section class="page page--cover">
  <div class="cover__waves" role="img" aria-label="Abstract flowing blue line waves on a dark navy background"></div>
  <div class="cover__client-logo">Client Logo</div>
  <h1 class="cover__title">30 Days<br>To Value</h1>
  <div class="cover__report">Report</div>
  <div class="cover__rule"></div>
  <p class="cover__subtitle">Your First Month of Progress</p>
  <div class="cover__meta">CLIENT: [Client Name]<br>DATE: [Month / Year]</div>
  <div class="cover__brand-box">
    <div class="brand"><span class="brand__square"></span><span class="brand__name">Cindermoor Care Allies</span></div>
  </div>
  <p class="cover__prepared"><span>PREPARED BY:</span>Cindermoor Care Allies</p>
</section>

<!-- Page 2: welcome -->
<section class="page page--welcome">
  <svg class="welcome__photo" viewBox="0 0 437 570" role="img" aria-label="Photo of two business people shaking hands over a café table with a coffee cup and tablet">
    <defs>
      <linearGradient id="photoTone" x1="0" y1="0" x2="1" y2="1">
        <stop offset="0" stop-color="#7a4a3e"/>
        <stop offset=".45" stop-color="#a7766a"/>
        <stop offset=".75" stop-color="#4a3a3a"/>
        <stop offset="1" stop-color="#1d2438"/>
      </linearGradient>
    </defs>
    <path d="M0,263 L220,263 C320,263 410,220 437,118 L437,570 L0,570 Z" fill="url(#photoTone)"/>
    <path d="M0,259 L220,259 C320,259 410,216 437,116" fill="none" stroke="var(--blue)" stroke-width="8"/>
  </svg>
  <header class="page-header">
    <div class="brand"><span class="brand__square"></span><span class="brand__name">Cindermoor Care Allies</span></div>
    <span class="page-header__tag">Day 1–30 progress</span>
  </header>
  <h2 class="section-title" style="left:45px; top:58px; font-size:23px;">Welcome &amp;<br>Overview Page</h2>
  <div class="welcome__body">
    <p>The first 30 days are about creating momentum. Our goal was to build the foundation for measurable growth — from your website and Mapstead Business Profile to your SEO systems, audits, and backlink strategy.</p>
    <p>This report highlights what’s been accomplished and what’s next in your marketing journey.</p>
  </div>
</section>

<!-- Page 3: highlights -->
<section class="page page--highlights">
  <div class="highlights__glow"></div>
  <header class="page-header">
    <div class="brand"><span class="brand__square"></span><span class="brand__name">Cindermoor Care Allies</span></div>
    <span class="page-header__tag">Day 1–30 progress</span>
  </header>
  <h2 class="section-title" style="left:46px; top:58px; font-size:23px;">Highlights &amp;<br>Quick Wins</h2>

  <article class="win-card" style="left:49px; top:157px;">
    <svg viewBox="0 0 32 32" aria-hidden="true"><path d="M26 4c-7 0-12 4-15 10l-4 1-3 4 5 0 4 4 0 5 4-3 1-4c6-3 10-8 10-15z" fill="var(--ink)"/><circle cx="19" cy="12" r="2.5" fill="var(--blue-card)"/><path d="M8 22l-4 6M10 24l-3 5M6 20l-3 4" stroke="var(--ink)" stroke-width="1.5"/></svg>
    <p class="win-card__text">Website launched and optimized for SEO</p>
  </article>
  <article class="win-card" style="left:168px; top:157px;">
    <svg viewBox="0 0 32 32" aria-hidden="true"><path d="M16 2a10 10 0 0 0-10 10c0 8 10 18 10 18s10-10 10-18A10 10 0 0 0 16 2z" fill="var(--ink)"/><circle cx="16" cy="12" r="4" fill="var(--blue-card)"/></svg>
    <p class="win-card__text">Mapstead Business Profiles verified and optimized</p>
  </article>
  <article class="win-card" style="left:287px; top:157px;">
    <svg viewBox="0 0 32 32" aria-hidden="true"><path d="M22 3l7 7-17 17-8 2 2-8z" fill="var(--ink)"/><path d="M20 5l7 7" stroke="var(--blue-card)" stroke-width="1.5"/></svg>
    <p class="win-card__text">Comprehensive SEO audits completed</p>
  </article>
  <article class="win-card win-card--low" style="left:49px; top:331px;">
    <svg viewBox="0 0 32 32" aria-hidden="true"><g fill="none" stroke="var(--ink)" stroke-width="4" stroke-linecap="round"><path d="M14 18l-5 5a4.5 4.5 0 0 1-6-6l5-5a4.5 4.5 0 0 1 6 0"/><path d="M18 14l5-5a4.5 4.5 0 0 1 6 6l-5 5a4.5 4.5 0 0 1-6 0"/><path d="M12 20l8-8"/></g></svg>
    <p class="win-card__text">Backlink strategy implementation underway</p>
  </article>
  <article class="win-card win-card--low" style="left:168px; top:331px;">
    <svg viewBox="0 0 32 32" aria-hidden="true"><rect x="4" y="7" width="21" height="21" fill="none" stroke="var(--ink)" stroke-width="2.5"/><path d="M8 13h10M8 18h13M8 23h13" stroke="var(--ink)" stroke-width="2"/><path d="M27 3l3 3-10 10-4 1 1-4z" fill="var(--ink)"/></svg>
    <p class="win-card__text">First blog articles published</p>
  </article>
  <article class="win-card win-card--low" style="left:287px; top:331px;">
    <svg viewBox="0 0 32 32" aria-hidden="true"><rect x="5" y="5" width="19" height="24" fill="none" stroke="var(--ink)" stroke-width="2.2"/><rect x="11" y="3" width="7" height="4" fill="var(--ink)"/><path d="M9 22v-4M13 22v-7M17 22v-5" stroke="var(--ink)" stroke-width="2.2"/><circle cx="23" cy="21" r="4" fill="none" stroke="var(--ink)" stroke-width="2"/><path d="M26 24l4 4" stroke="var(--ink)" stroke-width="2.5"/></svg>
    <p class="win-card__text">Tracking and analytics systems connected</p>
  </article>
</section>

<!-- Page 4: audits -->
<section class="page page--audits">
  <header class="page-header">
    <div class="brand"><span class="brand__square"></span><span class="brand__name">Cindermoor Care Allies</span></div>
    <span class="page-header__tag">Day 1–30 progress</span>
  </header>
  <h2 class="section-title" style="left:56px; top:58px; font-size:21.5px;">Comprehensive Audits<br>&amp; Strategy Development</h2>
  <p class="audits__intro">To ensure long-term results, our team conducted a full suite of technical and strategic audits during the first month. These insights guided your SEO roadmap and content strategy moving forward.</p>
  <h3 class="audits__heading">Audits &amp; Deliverables Completed:</h3>

  <div class="funnel-step" style="left:45px; width:346px; top:228px; clip-path:polygon(0 0,100% 0,95.4% 100%,4.6% 100%);">
    <span class="funnel-step__label">Technical SEO Audit:</span><span>Site health, indexation, and crawl efficiency</span></div>
  <div class="funnel-step" style="left:68px; width:300px; top:287px; clip-path:polygon(0 0,100% 0,94.7% 100%,5.3% 100%);">
    <span class="funnel-step__label">Backlink Audit:</span><span>Link quality, toxicity review, and<br>authority scoring</span></div>
  <div class="funnel-step" style="left:89px; width:259px; top:341px; clip-path:polygon(0 0,100% 0,94.6% 100%,4.6% 100%);">
    <span class="funnel-step__label">Competitor Analysis:</span><span>Top-ranking competitors’ content,<br>backlinks, and keyword profiles</span></div>
  <div class="funnel-step" style="left:108px; width:221px; top:393px; clip-path:polygon(0 0,100% 0,92.8% 100%,6.8% 100%);">
    <span class="funnel-step__label">On-Page SEO Audit:</span><span>Metadata, headings, internal links,<br>and content structure</span></div>
  <div class="funnel-step" style="left:129px; width:180px; top:447px; clip-path:polygon(0 0,100% 0,91.7% 100%,8.3% 100%);">
    <span class="funnel-step__label">Content Audit:</span><span>Keyword targeting, topical gaps,<br>and conversion opportunities</span></div>
  <div class="funnel-step" style="left:150px; width:137px; top:500px; clip-path:polygon(0 0,100% 0,89% 100%,11% 100%);">
    <span class="funnel-step__label">Strategy Development:</span><span>90-day SEO plan and keyword<br>roadmap created</span></div>
</section>

</body>
</html>
```